Crestline Forge Alloys Website

I need a redesign of my current website: www.crestlineforgealloys.example.
I would like to update the look, add some new stock photos of shiny stainless steel bar stock items. All of our grades of material should show on each page so that when people search for the grades on Google, our company site comes up. Most of the text content will be the same with some more changes. Also, we will want to add a button for calling our company for sales calls and one for sending a request for quote. I want the graphics to get prospects attention. I won't people to see us as a large stocking facility that is strong. Bold colors, silver, red, and blue.

Target Market(s)

Contract manufacturers, screw machine houses, medical instrument manufacturers, oil and gas parts industry, aerospace industry, automotive industry, food industry

Number of Pages Required

5+ page

Font styles to use
Sans Serif

Colors
ec1f27
0355a3

Requirements
Must have
• Pictures of stainless steel round bar. Also, a button linking someone to sales@crestlineforgealloys.example and our phone # 555-273-8640. Main stainless steel and titanium grades listed on each and every page. Also, a 1 page copy of our ISO 9001 certificatation.

```html
<!DOCTYPE html>
<html lang="en">
<head>
<meta charset="utf-8">
<title>Crestline Forge Alloys</title>
<link href="https://fonts.googleapis.com/css2?family=Open+Sans:ital,wght@0,400;0,600;0,700;1,400&family=Lora:ital@1&display=swap" rel="stylesheet">
<style>
:root{
  --red:#e4262b;
  --blue:#0d5fb5;
  --dark:#262626;
  --darker:#1d1d1d;
  --nav:#2f2f2f;
  --light:#ededed;
  --panel:#e3e3e3;
  --text:#444;
  --muted:#8a8a8a;
  --white:#fff;
}
*{margin:0;padding:0;box-sizing:border-box}
html,body{width:746px;height:1200px;overflow:hidden}
body{position:relative;font-family:"Open Sans",sans-serif;background:var(--light);color:var(--text)}
.abs{position:absolute}
a{color:inherit;text-decoration:none}

/* header */
.topbar{left:0;top:0;width:746px;height:56px;background:var(--dark)}
.brand{left:84px;top:13px;display:flex;align-items:center;gap:10px;color:var(--white);font-size:11px;font-weight:600}
.brand-mark{width:26px;height:26px;background:var(--red)}
.social{left:396px;top:23px;display:flex;gap:8px}
.social span{width:10px;height:10px;border-radius:50%;background:#777}
.login{left:481px;top:21px;width:74px;height:16px;background:#3a3a3a;color:#ddd;font-size:6.5px;font-weight:700;display:flex;align-items:center;justify-content:center;letter-spacing:.3px}
.search{left:572px;top:21px;width:90px;height:16px;background:#1f1f1f;border:1px solid #3a3a3a;color:#888;font-size:6.5px;display:flex;align-items:center;gap:5px;padding-left:7px}
.navbar{left:0;top:56px;width:746px;height:30px;background:var(--nav);border-top:1px solid #3a3a3a}
.nav{left:84px;top:0;height:29px;display:flex;font-size:7.5px;color:#ddd}
.nav a{padding:0 10px;line-height:29px}
.nav a.active{background:#242424;color:#fff;font-weight:600}
.tools{left:590px;top:6px;width:71px;height:16px;background:#444;color:#eee;font-size:6.5px;font-weight:700;display:flex;align-items:center;justify-content:center}

/* hero */
.hero{left:0;top:86px;width:746px;height:244px;background:radial-gradient(ellipse at 50% 40%,#5a554e 0%,#3b3834 55%,#242220 100%)}
.hero-title{left:0;width:746px;top:156px;text-align:center;color:#fff;font-size:17px;font-weight:700}
.hero-sub{left:0;width:746px;top:186px;text-align:center;color:#c9c3b4;font-size:12.5px}
.hero-btn{left:312px;top:227px;width:122px;height:32px;background:var(--blue);color:#fff;font-size:11.5px;font-weight:600;display:flex;align-items:center;justify-content:center}
.arrow{top:190px}

/* info band */
.info{left:0;top:330px;width:746px;height:166px;background:#eeeeee;border-top:3px solid #cfcfcf}
.divider{top:330px;width:1px;height:166px;background:#d6d6d6}
.label{font-size:7.5px;font-weight:700;color:#555;letter-spacing:.3px}
.small{font-size:8.5px;color:var(--muted);line-height:13px}
.date{font-size:6.5px;color:#aaa}
.zip{left:84px;top:409px;width:120px;height:23px;background:#fff;border:1px solid #e2e2e2;font-size:7px;color:#aaa;display:flex;align-items:center;gap:6px;padding-left:9px}
.link{font-size:7.5px;color:var(--red);font-weight:600;display:flex;align-items:center;gap:30px}
.video{left:298px;top:399px;width:149px;height:47px;background:linear-gradient(#c9c7c0,#a9a59a)}

/* deal with */
.deal-bg{left:0;top:496px;width:746px;height:180px;background:var(--panel)}
.deal-panel{left:58px;top:503px;width:645px;height:165px;background:#e9e9e9}
.h-sec{font-size:10px;font-weight:700;color:#555}
.tile{top:553px;width:138px;height:104px}
.tile-label{color:#fff;font-size:8.5px;font-weight:700;display:flex;align-items:center;justify-content:center}

/* about + testimonial */
.h2{font-size:15.5px;font-weight:600;color:#222}
.h2 em{font-style:normal;color:var(--red)}
.about-img{left:85px;top:719px;width:350px;height:92px;background:linear-gradient(#8a3e2e 0%,#b9b6b0 35%,#d9d8d4 70%,#9e9c98 100%)}
.about-lead{left:84px;top:821px;width:360px;font-size:9.5px;font-weight:600;color:#222}
.about-text{left:84px;top:840px;width:352px;font-size:7px;line-height:10.5px;color:#666}
.quote{left:463px;top:721px;width:204px;height:101px;background:#dedede;border:1px solid #d4d4d4;padding:14px 16px 0 30px;font-family:"Lora",serif;font-style:italic;font-size:8.8px;line-height:15px;color:#666}
.qmark{left:473px;top:724px;font-family:"Lora",serif;font-size:16px;color:#aaa}
.avatar{left:476px;top:832px;width:38px;height:38px;border-radius:50%;background:#d0d0d0;border:3px solid #f2f2f2}
.name{left:521px;top:839px;font-size:8px;font-weight:700;color:#333}
.role{left:521px;top:850px;font-family:"Lora",serif;font-style:italic;font-size:6.5px;color:#999}

/* group */
.group{left:0;top:916px;width:746px;height:118px;background:#e5e5e5;border-top:1px solid #d8d8d8}
.badge{top:980px;height:30px;background:#9a9a9a;opacity:.6}

/* footer */
.footer{left:0;top:1034px;width:746px;height:142px;background:var(--dark)}
.fcol h4{font-size:9px;font-weight:600;color:#fff;margin-bottom:10px}
.fcol li{list-style:none;font-size:7.5px;line-height:11.7px;color:#e2e2e2}
.fcol.wide li{line-height:16px;padding-left:6px}
.mail{left:522px;top:1077px;width:102px;height:21px;background:#fff;font-size:7px;color:#333;display:flex;align-items:center;padding-left:5px}
.join{left:624px;top:1077px;width:37px;height:21px;background:var(--red);color:#fff;font-size:8px;font-weight:700;display:flex;align-items:center;justify-content:center}
.copy{left:0;top:1176px;width:746px;height:24px;background:var(--darker);color:#bbb;font-size:7.5px;display:flex;align-items:center;justify-content:center}
</style>
</head>
<body>

<header>
  <div class="abs topbar"></div>
  <div class="abs brand"><span class="brand-mark"></span>Crestline Forge Alloys</div>
  <div class="abs social"><span></span><span></span><span></span><span></span></div>
  <div class="abs login">EMPLOYEE LOGIN</div>
  <div class="abs search">
    <svg width="7" height="7" viewBox="0 0 10 10"><circle cx="4" cy="4" r="3" fill="none" stroke="#aaa" stroke-width="1.4"/><line x1="6.3" y1="6.3" x2="9" y2="9" stroke="#aaa" stroke-width="1.4"/></svg>
    Search CFA...
  </div>
  <div class="abs navbar">
    <nav class="abs nav">
      <a class="active">Home</a><a>Products</a><a>Quality</a><a>Locations</a><a>Services</a><a>Large volume</a><a>Inquiries</a><a>FAQ</a>
    </nav>
    <div class="abs tools">ONLINE TOOLS &nbsp;▾</div>
  </div>
</header>

<section>
  <div class="abs hero" role="img" aria-label="Dark photograph of stainless steel bar stock"></div>
  <svg class="abs arrow" style="left:31px" width="10" height="14" viewBox="0 0 10 14"><polyline points="8,1 2,7 8,13" fill="none" stroke="#888" stroke-width="2.5"/></svg>
  <svg class="abs arrow" style="left:704px" width="10" height="14" viewBox="0 0 10 14"><polyline points="2,1 8,7 2,13" fill="none" stroke="#888" stroke-width="2.5"/></svg>
  <h1 class="abs hero-title">The Best Delar At Crestline Forge Alloys</h1>
  <p class="abs hero-sub">Point. Click. Parts. No step four.</p>
  <a class="abs hero-btn">Read More</a>
</section>

<section>
  <div class="abs info"></div>
  <div class="abs divider" style="left:275px"></div>
  <div class="abs divider" style="left:471px"></div>

  <div class="abs label" style="left:84px;top:353px">STORE LOCATOR</div>
  <p class="abs small" style="left:84px;top:373px;width:110px">Find your nearest dealer by zip code.</p>
  <div class="abs zip">
    <svg width="7" height="10" viewBox="0 0 8 11"><path d="M4 0.5a3.5 3.5 0 0 1 3.5 3.5c0 2.6-3.5 6.5-3.5 6.5S0.5 6.6 0.5 4A3.5 3.5 0 0 1 4 0.5z" fill="#bbb"/><circle cx="4" cy="4" r="1.3" fill="#fff"/></svg>
    Enter your ZIP...
  </div>
  <a class="abs link" style="left:84px;top:462px">Browse all location <svg width="10" height="10" viewBox="0 0 10 10"><circle cx="5" cy="5" r="4.3" fill="none" stroke="#e4262b"/><polyline points="4,3 6,5 4,7" fill="none" stroke="#e4262b"/></svg></a>

  <div class="abs label" style="left:276px;width:195px;text-align:center;top:353px">PRODUCT HIGHLIGHT</div>
  <p class="abs small" style="left:276px;width:195px;text-align:center;top:373px">See the RX-40 in action.</p>
  <div class="abs video" role="img" aria-label="Video still of heavy equipment in the field"></div>
  <svg class="abs" style="left:363px;top:413px" width="19" height="19" viewBox="0 0 20 20"><circle cx="10" cy="10" r="8.5" fill="none" stroke="#fff" stroke-width="1.2" opacity=".8"/><polygon points="8,6 14,10 8,14" fill="#fff" opacity=".8"/></svg>
  <a class="abs link" style="left:326px;top:462px">View all highlights <svg width="10" height="10" viewBox="0 0 10 10"><circle cx="5" cy="5" r="4.3" fill="none" stroke="#e4262b"/><polyline points="4,3 6,5 4,7" fill="none" stroke="#e4262b"/></svg></a>

  <div class="abs label" style="right:84px;top:353px">CFA NEWS</div>
  <div class="abs" style="right:84px;top:373px;text-align:right;width:180px">
    <p class="small">Ridgeway Visitor Center Opens</p>
    <p class="date" style="margin-bottom:9px">Oct 19, 2012</p>
    <p class="small">CFA Ridgeway Hits the Road with the NEW Ridgeway Vocational Truck</p>
    <p class="date">Oct 19, 2012</p>
  </div>
  <a class="abs link" style="right:84px;top:462px;gap:19px">All news &amp; events <svg width="10" height="10" viewBox="0 0 10 10"><circle cx="5" cy="5" r="4.3" fill="none" stroke="#e4262b"/><polyline points="4,3 6,5 4,7" fill="none" stroke="#e4262b"/></svg></a>
</section>

<section>
  <div class="abs deal-bg"></div>
  <div class="abs deal-panel"></div>
  <h3 class="abs h-sec" style="left:84px;top:524px">WE ARE DEAL WITH</h3>
  <a class="abs" style="left:628px;top:526px;font-size:7px;font-weight:600;color:#888">VIEW ALL</a>
  <div class="abs tile" style="left:84px;background:linear-gradient(135deg,#6f7275,#c3c5c6 50%,#5c5f62)" role="img" aria-label="Screw machine turning bar stock"></div>
  <div class="abs tile tile-label" style="left:231px;background:#2b2b2b">Medical Instrument</div>
  <div class="abs tile" style="left:378px;background:linear-gradient(#3c6fb0 0%,#9fb3c8 40%,#a8aaab 100%)" role="img" aria-label="Stainless steel tanks at a food plant"></div>
  <div class="abs tile" style="left:525px;background:linear-gradient(#d7d9db,#a9adb0 60%,#8d9194)" role="img" aria-label="Stainless steel commercial kitchen"></div>
</section>

<section>
  <h2 class="abs h2" style="left:84px;top:688px">About <em>Crestline Forge Alloys</em></h2>
  <div class="abs about-img" role="img" aria-label="Rows of polished stainless steel parts on a production floor"></div>
  <p class="abs about-lead">Crestline Forge Alloys is a national distributor specializing in the distribution</p>
  <p class="abs about-text">of stainless steel titanium, and aluminum bar stock, sheet, plate, pipe, tubing, wire, and coil. We have 7 stocking facilities throughout the country offering 1-2 day delivery on stock items to virtually any area of the U.S.A.</p>
  <a class="abs link" style="left:84px;top:877px;gap:6px">Read More <svg width="12" height="6" viewBox="0 0 12 6"><line x1="0" y1="3" x2="11" y2="3" stroke="#e4262b"/><polyline points="8,0.5 11,3 8,5.5" fill="none" stroke="#e4262b"/></svg></a>

  <h2 class="abs h2" style="left:462px;top:688px">Our <em>Testimonial</em></h2>
  <blockquote class="abs quote">We provide you with the ability to have projects delivered in record time, keeping disruption to building operations and tenants to an absolute minimum.</blockquote>
  <span class="abs qmark">“</span>
  <div class="abs avatar" role="img" aria-label="Client portrait placeholder"></div>
  <div class="abs name">MR. T.</div>
  <div class="abs role">Harbor Build Services</div>
  <a class="abs link" style="left:521px;top:861px;gap:6px">Read More <svg width="12" height="6" viewBox="0 0 12 6"><line x1="0" y1="3" x2="11" y2="3" stroke="#e4262b"/><polyline points="8,0.5 11,3 8,5.5" fill="none" stroke="#e4262b"/></svg></a>
</section>

<section>
  <div class="abs group"></div>
  <div class="abs label" style="left:0;width:746px;text-align:center;top:943px;color:#666">THE CFA GROUP</div>
  <div class="abs badge" style="left:118px;width:62px"></div>
  <div class="abs badge" style="left:210px;width:70px"></div>
  <div class="abs badge" style="left:304px;width:76px"></div>
  <div class="abs badge" style="left:406px;width:78px"></div>
  <div class="abs badge" style="left:509px;width:35px"></div>
  <div class="abs badge" style="left:567px;width:56px"></div>
</section>

<footer>
  <div class="abs footer"></div>
  <div class="abs fcol" style="left:84px;top:1054px"><h4>About Store</h4><ul><li>Lorem ipsum dolor</li><li>Sit amet consectetur</li><li>Adipiscing elit,</li><li>Sed do euismod</li><li>Tempor incidunt</li><li>Labore et dolor</li><li>Magna aliqua.</li></ul></div>
  <div class="abs fcol" style="left:203px;top:1054px"><h4>Categories</h4><ul><li>Lorem ipsum</li><li>Is simply dummy</li><li>Text of the</li><li>Printing</li><li>And typesrtting</li><li>Industry</li></ul></div>
  <div class="abs fcol wide" style="left:309px;top:1054px"><h4>Sitquet amer</h4><ul><li>About Us</li><li>Brands</li><li>Stockist</li><li>News</li><li>Contact Us</li></ul></div>
  <div class="abs fcol" style="left:415px;top:1054px"><h4>Amet dolor</h4><ul><li>Lorem ipsum</li><li>Is simply dummy</li><li>Text of the</li><li>Printing</li><li>And typesrtting</li><li>Industry</li></ul></div>
  <div class="abs fcol" style="left:524px;top:1054px"><h4>Join Our Mailing List</h4></div>
  <div class="abs mail">Enter your email address...</div>
  <div class="abs join">JOIN</div>
  <div class="abs copy">Copyrights © 2014 &nbsp;- All Rights Reserved</div>
</footer>

</body>
</html>
```